Very Simple Web Redesign Project - Using Photoshop

Required is a very simple website home page redesign for the following site: http://www.kestrelslateworks.com.au/
I require this as a Photoshop design.
The basic look and feel of the site needs to remain.
Specifically the colours don't need to be changed.
The positioning of the site is currently correct for the target market.
The site does not need to be made super slick looking. Just upgraded to a new version.
The current text can all be used.
The only menus necessary are a horizontal menu at the top, and a simple horizontal text menu at the bottom of the page. Do NOT retain the vertical menu on the home page (having the items "Our Gallery", "Our Services", "Enquire Now").
Give the horizontal menu the following items:
Home | Slate Roof Repairs | Slate Reroofing | Slate Roof Benefits | Other Services | Photo Gallery | FAQ's | Free Quote | Contact Us
The picture of the house at the top RHS of the page needs to be reduced in size by approx 50% and moved to the top LHS of the page.
Please place the following text into the top of the page:
"Call Now: 0427 618 302"
Keep the four pictures on the home page layout. Some larger images attached.
Thanks,
Ned
Updates
Hi,
Thanks for all the designs.
I am working with my client to get which one they like the most.
Thanks,
Ned

```html
<!DOCTYPE html>
<html lang="en">
<head>
<meta charset="utf-8">
<title>Kestrel Slateworks – The Slate Roof Specialists</title>
<link rel="stylesheet" href="https://fonts.googleapis.com/css2?family=Arimo:wght@400;700&display=swap">
<style>
:root{
  --green-dark:#1f5200;
  --green-mid:#3a7d00;
  --green-bright:#5a9e0a;
  --green-light:#7cbc1e;
  --nav-bg:#1e4a00;
  --side-bg:#333333;
  --page-bg:#ffffff;
  --text:#222222;
  --heading:#5a9a10;
  --link:#4f8f0a;
}
*{box-sizing:border-box;margin:0;padding:0}
html,body{width:1200px;height:900px;overflow:hidden}
body{position:relative;background:var(--side-bg);font-family:"Arimo",Arial,sans-serif;color:var(--text)}
.site-header{position:absolute;left:0;top:0;width:1200px;height:144px;background:linear-gradient(180deg,#2f6a00 0%,#3d8400 100%);overflow:hidden}
.site-header svg.swoosh{position:absolute;left:0;top:0}
.brand{position:absolute;left:80px;top:30px;display:flex;align-items:center;gap:26px}
.brand-mark{width:76px;height:76px;background:var(--green-dark);border-radius:6px}
.brand-name{font-family:"Arimo",Arial,sans-serif;font-weight:400;font-size:54px;color:#ffffff;letter-spacing:0.5px}
.call-box{position:absolute;left:885px;top:29px;width:232px;height:92px;border:3px solid #a8dd55;border-radius:8px;background:linear-gradient(180deg,#5ea912,#3f8400);color:#fff;text-align:center;box-shadow:0 2px 4px rgba(0,0,0,.4)}
.call-box .label{display:block;font-weight:700;font-size:24px;margin-top:10px;letter-spacing:1px}
.call-box .number{display:block;font-size:29px;margin-top:4px;letter-spacing:1px}
.main-nav{position:absolute;left:0;top:144px;width:1200px;height:28px;background:var(--nav-bg);border-bottom:3px solid var(--green-light);text-align:center;font-size:15px;color:#fff;line-height:26px}
.main-nav a{color:#fff;text-decoration:none}
.main-nav .sep{margin:0 7px}
.page{position:absolute;left:149px;top:175px;width:902px;height:719px;background:var(--page-bg);box-shadow:0 0 18px rgba(0,0,0,.6)}
.photo-strip{position:absolute;left:0;top:214px;width:1200px;height:226px}
.photo{position:absolute;top:0;height:226px;border:4px solid #fff;box-shadow:2px 3px 8px rgba(0,0,0,.5)}
.photo.p1{left:42px;width:197px;background:linear-gradient(160deg,#b9cbe0 0%,#5a5c66 40%,#6d6f70 80%,#3f4a3a 100%)}
.photo.p2{left:252px;width:221px;background:linear-gradient(170deg,#6c8a4a 0%,#6a5f66 45%,#76616b 75%,#c9a27a 100%)}
.photo.p3{left:486px;width:197px;background:linear-gradient(160deg,#4b4752 0%,#5e5565 50%,#4a4250 100%)}
.photo.p4{left:696px;width:256px;background:linear-gradient(180deg,#c7d6e6 0%,#5a5e5f 35%,#333 70%,#4e6a36 100%)}
.photo.p5{left:964px;width:194px;background:linear-gradient(160deg,#7a4a3c 0%,#5e6468 30%,#6f7570 100%)}
.quote-panel{position:absolute;left:185px;top:483px;width:256px;height:358px;border-radius:4px;background:linear-gradient(180deg,#3c7d00 0%,#2b6500 60%,#3f8a05 100%);color:#fff;overflow:hidden}
.quote-panel svg{position:absolute;left:0;top:0}
.quote-panel .inner{position:relative;padding:20px 27px 0 27px}
.quote-panel h2{font-size:16px;font-weight:400;text-align:center;line-height:20px;margin-bottom:14px}
.quote-panel h2 strong{font-weight:700}
.quote-panel p.area{font-size:15.5px;line-height:18.5px;margin-bottom:30px}
.quote-panel p.contact{font-size:15.5px;font-weight:700;line-height:20px;letter-spacing:.3px;margin-bottom:16px}
.quote-panel p.reg{font-size:13px;line-height:16px}
.intro{position:absolute;left:470px;top:488px;width:550px}
.intro h1{font-size:23px;font-weight:700;color:var(--heading);margin-bottom:15px;letter-spacing:.3px}
.intro p{font-size:14px;line-height:17px;margin-bottom:17px}
.intro a{color:var(--link)}
.site-footer{position:absolute;left:174px;top:864px;width:840px;font-size:12px;display:flex;justify-content:space-between}
.footer-nav a{color:var(--text);text-decoration:none;margin-left:6px}
.footer-nav a.current{color:var(--link)}
.base-line{position:absolute;left:0;top:894px;width:1200px;height:6px;background:var(--green-mid);border-top:1px solid var(--green-light)}
</style>
</head>
<body>
<header class="site-header">
  <svg class="swoosh" width="1200" height="144" viewBox="0 0 1200 144" aria-hidden="true">
    <path d="M0 60 C250 70 520 160 900 144 L0 144 Z" fill="#4c9a0a" opacity=".55"/>
    <path d="M0 96 C300 100 600 160 860 144 L0 144 Z" fill="#2a5e00" opacity=".5"/>
  </svg>
  <div class="brand">
    <span class="brand-mark"></span>
    <span class="brand-name">Kestrel Slateworks</span>
  </div>
  <div class="call-box">
    <span class="label">CALL NOW:</span>
    <span class="number">0427 618 302</span>
  </div>
</header>
<nav class="main-nav">
  <a href="#">Home</a><span class="sep">|</span><a href="#">Slate Roof Repairs</a><span class="sep">|</span><a href="#">Slate Reroofing</a><span class="sep">|</span><a href="#">Slate Roof Benefits</a><span class="sep">|</span><a href="#">Other Services</a><span class="sep">|</span><a href="#">Photo Gallery</a><span class="sep">|</span><a href="#">FAQ's</a><span class="sep">|</span><a href="#">Free Quote</a><span class="sep">|</span><a href="#">Contact Us</a>
</nav>
<div class="page"></div>
<div class="photo-strip">
  <div class="photo p1" role="img" aria-label="Slate roof with white gable trim on a period house"></div>
  <div class="photo p2" role="img" aria-label="Conical slate turret roof with finial"></div>
  <div class="photo p3" role="img" aria-label="Slate roof with small dormer window"></div>
  <div class="photo p4" role="img" aria-label="Re-roofed slate house with front porch"></div>
  <div class="photo p5" role="img" aria-label="Close view of weathered slate tiles near a downpipe"></div>
</div>
<aside class="quote-panel">
  <svg width="256" height="358" viewBox="0 0 256 358" aria-hidden="true">
    <path d="M0 250 C80 190 180 180 256 200 L256 358 L0 358 Z" fill="#4d9a0c" opacity=".45"/>
  </svg>
  <div class="inner">
    <h2>Call now and arrange a<br><strong>FREE QUOTE!</strong></h2>
    <p class="area">We service all inner city suburbs of Sydney roughly covering an area encompassing Gordon to Epping, Mosman to Bondi, Coogee to Kogarah and Kingsgrove to Burwood and Concord.</p>
    <p class="contact">Mobile: 0427 618 302<br>Fax: 02 8155 4620</p>
    <p class="reg">Abn 47 306 219 884<br>Lic No. 204817K</p>
  </div>
</aside>
<main class="intro">
  <h1>Kestrel Slateworks: The Slate Roof Specialists</h1>
  <p>At Kestrel Slateworks we specialize in the upkeep, maintenance, repair and replacement of all types of slate roof as well as wood shingles. We can track down the leak that just won't go away or give your house a complete re-roof. We can also provide all your guttering needs.</p>
  <p>Kestrel Slateworks is a small company and as such we do not have the overheads that larger companies do. Quality work and attention to detail are our trade-mark.</p>
  <p>All photos on this website consist of work which I have personally done. The above photos provide at a quick glance a reasonable cross section of the type of work I do.</p>
  <p>By clicking on the <a href="#">Photo Gallery</a> link you can see other work including some before and after shots.</p>
  <p>Feel free to call at your earliest convenience to organise an obligation free quote or fill out a form by clicking on <a href="#">Contact Us</a>.</p>
</main>
<footer class="site-footer">
  <span>© 20011 Kestrel Slateworks</span>
  <nav class="footer-nav"><a class="current" href="#">Home</a><a href="#">Free Qoute</a><a href="#">Contact Us</a></nav>
</footer>
<div class="base-line"></div>
</body>
</html>
```